Creative, Striking, Responsive Tutoring Flyer

I need a designer superstar to create an attractive, modern and eye-catching flyer for me. I'm a teacher and I need the flyer to sell French & German private lessons.

Attached is an example that I like a lot. Please create a similar design.

```html
<!DOCTYPE html>
<html lang="en">
<head>
<meta charset="utf-8">
<title>French &amp; German Private Lessons</title>
<link rel="stylesheet" href="https://fonts.googleapis.com/css2?family=Caveat:wght@500;700&family=Open+Sans:wght@400;600;700;800&display=swap">
<style>
  :root {
    --page-bg: #eef2f5;
    --sky: #3a8fd0;
    --sky-light: #a9d8f2;
    --sun: #fbb540;
    --navy: #0d2a4d;
    --ring: #1d5486;
    --white: #ffffff;
    --chalk-white: #f4f4f0;
    --chalk-yellow: #e3d64a;
    --board-dark: #0f1d16;
    --board-mid: #1f3328;
    --frame: #4a2e1c;
  }
  * { margin: 0; padding: 0; box-sizing: border-box; }
  html, body { width: 900px; height: 1200px; overflow: hidden; }
  body { background: var(--page-bg); font-family: "Open Sans", sans-serif; color: var(--navy); position: relative; }

  .flyer { position: absolute; left: 45px; top: 25px; width: 810px; height: 1149px; overflow: hidden; background: var(--white); }
  .flyer-backdrop { position: absolute; inset: 0; width: 100%; height: 100%; }

  .chalkboard {
    position: absolute; left: 36px; top: 24px; width: 739px; height: 544px;
    border: 24px solid var(--frame); border-radius: 6px; overflow: hidden;
  }
  .chalkboard-art {
    position: absolute; inset: 0;
    background: radial-gradient(ellipse at 50% 50%, var(--board-mid), var(--board-dark));
  }
  .board-title {
    position: absolute; left: 20px; top: 150px; width: 650px;
    font-family: "Caveat", cursive; font-weight: 700; font-size: 112px; line-height: 1;
    color: var(--chalk-white); text-align: center; white-space: nowrap;
    transform: rotate(-2deg);
  }
  .board-subtitle {
    position: absolute; left: 180px; top: 262px; width: 330px;
    font-family: "Caveat", cursive; font-weight: 500; font-size: 74px; line-height: 1;
    color: var(--chalk-yellow); text-align: center; white-space: nowrap;
  }

  .audience { position: absolute; left: 41px; top: 583px; line-height: 1.2; }
  .audience-intro { font-size: 39px; font-weight: 400; }
  .audience-list { font-size: 37px; font-weight: 400; }
  .audience-list strong { font-weight: 800; }

  .promise {
    position: absolute; left: 424px; top: 694px; width: 325px; height: 65px;
    background: var(--sun); border-radius: 33px;
    font-size: 25px; font-weight: 700; line-height: 1.08; text-align: center;
    display: flex; align-items: center; justify-content: center;
  }

  .levels { position: absolute; left: 36px; top: 737px; list-style: none; }
  .level {
    width: 186px; height: 59px; margin-bottom: 23px; border-radius: 30px;
    background: var(--navy); color: var(--white);
    font-size: 22px; font-weight: 600; letter-spacing: 0.3px;
    display: flex; align-items: center; justify-content: center;
  }

  .photos { position: absolute; inset: 0; width: 100%; height: 100%; pointer-events: none; }

  .contact { position: absolute; left: 36px; top: 996px; list-style: none; }
  .contact-item { display: flex; align-items: center; height: 44px; font-size: 24px; font-weight: 700; }
  .contact-icon { width: 30px; height: 30px; margin-right: 11px; flex: none; }
</style>
</head>
<body>
  <main class="flyer">
    <svg class="flyer-backdrop" viewBox="0 0 1196 1696" preserveAspectRatio="none" aria-hidden="true">
      <path fill="var(--sky-light)" d="M820 830 C700 1000 570 1300 540 1696 L1196 1696 L1196 300 C1150 600 960 700 820 830 Z"/>
      <path fill="none" stroke="var(--sun)" stroke-width="5" d="M820 830 C700 1000 570 1300 540 1696"/>
      <path fill="none" stroke="var(--sun)" stroke-width="7" d="M940 30 C1080 0 1196 60 1196 60"/>
      <path fill="none" stroke="var(--sun)" stroke-width="7" d="M1196 380 C1180 450 1160 520 1140 560"/>
      <path fill="none" stroke="var(--sun)" stroke-width="26" d="M535 840 C500 1150 320 1480 0 1590"/>
      <path fill="var(--sky)" d="M0 0 H1020 C930 300 620 600 530 840 C480 1150 300 1450 0 1570 Z"/>
      <circle cx="870" cy="1405" r="253" fill="none" stroke="var(--ring)" stroke-width="3"/>
      <circle cx="873" cy="1405" r="208" fill="var(--ring)"/>
      <circle cx="648" cy="1305" r="140" fill="var(--ring)"/>
    </svg>

    <header class="chalkboard">
      <div class="chalkboard-art" role="img" aria-label="Chalkboard photo with green, orange and yellow pencils, reading glasses and an eraser"></div>
      <h1 class="board-title">French e German</h1>
      <p class="board-subtitle">private lessons</p>
    </header>

    <section class="audience">
      <p class="audience-intro">Private lessons for:</p>
      <p class="audience-list"><strong>children</strong>, <strong>teenagers</strong> and <strong>adults</strong></p>
    </section>

    <p class="promise">with private lessons<br>you learn much faster</p>

    <ul class="levels">
      <li class="level">BEGINNER</li>
      <li class="level">INTERMEDIATE</li>
      <li class="level">ADVANCED</li>
    </ul>

    <svg class="photos" viewBox="0 0 810 1149">
      <circle cx="439" cy="884" r="87" fill="#c9d3de" role="img" aria-label="Photo of a young boy reading a book"/>
      <circle cx="591" cy="951" r="129" fill="#e4e6e8" role="img" aria-label="Photo of a young woman with glasses reading"/>
    </svg>

    <ul class="contact">
      <li class="contact-item">
        <svg class="contact-icon" viewBox="0 0 24 24"><path fill="var(--navy)" d="M12 1C7.6 1 4.5 4.3 4.5 8.5 4.5 14 12 23 12 23s7.5-9 7.5-14.5C19.5 4.3 16.4 1 12 1zm0 10.5a3 3 0 1 1 0-6 3 3 0 0 1 0 6z"/></svg>
        Your Complete Address
      </li>
      <li class="contact-item">
        <svg class="contact-icon" viewBox="0 0 24 24"><path fill="var(--navy)" d="M6.6 10.8a15.2 15.2 0 0 0 6.6 6.6l2.2-2.2c.3-.3.7-.4 1-.2 1.1.4 2.3.6 3.6.6.6 0 1 .4 1 1V20c0 .6-.4 1-1 1C10.6 21 3 13.4 3 4c0-.6.4-1 1-1h3.5c.6 0 1 .4 1 1 0 1.3.2 2.5.6 3.6.1.3 0 .7-.2 1l-2.3 2.2z"/></svg>
        123.456.789
      </li>
      <li class="contact-item">
        <svg class="contact-icon" viewBox="0 0 24 24"><circle cx="12" cy="12" r="9" fill="none" stroke="var(--navy)" stroke-width="2.4"/></svg>
        @lingua_tutor_amelie
      </li>
    </ul>
  </main>
</body>
</html>
```